Aerial photo/video drone company needs new business card

Aerial visual company who offers photos and video services via drones.

We are KTO certified and work in the real estate, insurance, construction, and film industries.

I'm looking for a clean, professional, maybe even edgy design, that will be a conversation starter when networking.

I've included our logo, current business card, and font.

Our current business card is decent; albeit, I'm looking for something more unique. If you folks provide good designs, I'll definitely guarantee payment (and I'm not opposed to tipping if the design is above and beyond).

Target Market(s)

Insurance companies, real estate agents, construction companies, advertising & other creative agencies, and filmmakers/producers.

Industry/Entity Type

Business

Contact Information for Business Card

Company name pronounced tol-u-mo.

Other font styles liked:
• Font was uploaded; that or similar; not opposed to other fonts if they work well with the design

Requirements
Must have
• Clearly prominent logo; my name and title; phone number; email address; web address; mentioned "KTO Certified" or similar; should indicate "Aerial visual"
Nice to have
• Watermark of logo or otherwise
Should not have
• Pictures of drones or scenic shots

```html
<!DOCTYPE html>
<html lang="en">
<head>
<meta charset="utf-8">
<title>tolumo business card</title>
<link rel="stylesheet" href="https://fonts.googleapis.com/css2?family=Lexend:wght@400;500;600&display=swap">
<style>
  :root {
    --navy: #243a5e;
    --navy-deep: #22375a;
    --navy-soft: #2b4670;
    --sky: #2b8fd6;
    --ink: #25385b;
    --paper: #ffffff;
    --backdrop: #e9ebee;
  }
  * { margin: 0; padding: 0; box-sizing: border-box; }
  html, body { width: 1200px; height: 1000px; overflow: hidden; }
  body {
    background: var(--backdrop);
    font-family: "Lexend", "Helvetica Neue", Arial, sans-serif;
    color: var(--ink);
    position: relative;
  }
  .card {
    position: absolute;
    left: 265px;
    width: 667px;
    height: 397px;
    box-shadow: 0 4px 14px rgba(0,0,0,0.18);
    overflow: hidden;
  }
  .card-front { top: 74px; background: var(--paper); }
  .card-back { top: 533px; background: var(--navy); }

  .brand-mark {
    position: absolute;
    left: 130px; top: 31px;
    width: 60px; height: 60px;
    border-radius: 50%;
    background: var(--sky);
  }
  .brand-name {
    position: absolute;
    left: 31px; top: 92px;
    font-size: 64px;
    font-weight: 600;
    letter-spacing: 0.5px;
    line-height: 1;
    color: var(--navy);
  }
  .certification {
    position: absolute;
    left: 33px; top: 199px;
    font-size: 16px;
    font-weight: 600;
  }
  .contact-list {
    position: absolute;
    left: 33px; top: 230px;
    list-style: none;
    font-size: 16px;
    line-height: 24px;
  }
  .contact-list li { display: flex; align-items: center; gap: 6px; }
  .contact-list svg { width: 15px; height: 15px; fill: var(--sky); }
  .services {
    position: absolute;
    left: 33px; top: 309px;
    font-size: 15px;
    line-height: 19px;
  }
  .holder {
    position: absolute;
    right: 33px; top: 175px;
    text-align: right;
  }
  .holder-name { font-size: 21px; font-weight: 600; color: var(--navy); }
  .holder-title { font-size: 16px; color: var(--sky); margin-top: 2px; }

  .footer-band { position: absolute; left: 0; bottom: 0; width: 667px; height: 32px; }
  .social {
    position: absolute;
    left: 31px; bottom: 6px;
    display: flex; align-items: center; gap: 8px;
    color: var(--paper);
    font-size: 15px;
  }
  .social-dot { width: 18px; height: 18px; border-radius: 50%; background: var(--paper); }

  .back-pattern {
    position: absolute; inset: 0;
    background: linear-gradient(135deg, var(--navy-deep), var(--navy-soft) 50%, var(--navy-deep));
  }
  .back-name {
    position: absolute;
    left: 0; right: 0; top: 142px;
    text-align: center;
    font-size: 100px;
    font-weight: 600;
    line-height: 1;
    color: var(--paper);
  }
</style>
</head>
<body>
  <section class="card card-front">
    <div class="brand-mark"></div>
    <div class="brand-name">tolumo</div>

    <p class="certification">KTO Certified</p>
    <ul class="contact-list">
      <li><svg viewBox="0 0 16 16"><path d="M3 2h3l1.5 3.5-2 1.2a8 8 0 0 0 3.8 3.8l1.2-2L14 10v3a1 1 0 0 1-1 1A11 11 0 0 1 2 3a1 1 0 0 1 1-1z"/></svg>415.302.7781</li>
      <li><svg viewBox="0 0 16 16"><path d="M1 4h14v9H1z M1 4l7 5 7-5" fill="none" stroke="#2b8fd6" stroke-width="1.6"/></svg>dan@tolumo.com</li>
      <li><svg viewBox="0 0 16 16"><circle cx="8" cy="8" r="6.5" fill="none" stroke="#2b8fd6" stroke-width="1.6"/><path d="M1.5 8h13M8 1.5c-3 3.5-3 9.5 0 13M8 1.5c3 3.5 3 9.5 0 13" fill="none" stroke="#2b8fd6" stroke-width="1.2"/></svg>www.tolumo.com</li>
    </ul>
    <p class="services">Aerial Visual for<br>Real Estate / Insurance / Contruction / Film</p>

    <div class="holder">
      <p class="holder-name">Daniel K. Varga</p>
      <p class="holder-title">Pilot in Command</p>
    </div>

    <svg class="footer-band" viewBox="0 0 667 32" preserveAspectRatio="none">
      <polygon points="0,0 405,0 383,32 0,32" fill="#243a5e"/>
      <polygon points="411,0 667,0 667,32 389,32" fill="#2b8fd6"/>
    </svg>
    <div class="social"><span class="social-dot"></span>@tolumo</div>
  </section>

  <section class="card card-back">
    <div class="back-pattern" role="img" aria-label="Repeating brand-symbol pattern in soft navy tones"></div>
    <div class="back-name">tolumo</div>
  </section>
</body>
</html>
```